Online Art Gallery & Art Management Firm looking for a business card

I'm launching an online art gallery (paintings, photography, drawings, furniture, books, ...) where people can buy all types of art. It's a platform where young and unknown artists can showcase their oeuvre.

Additionally, the venture will act as my advising company for artists. I help them out with their business side of life and become their representative.

The company name: The Velvet Parlour
Logo is attached

I'm looking for something very classy and upmarket.
Updates

Reason: Logo wasn't finished yet...

The design should include the following information: - Name: Pieter Vandomme - Title: Founder - Mobile: +32 (0) 486 514 362 - E-mail: pieter@velvet-parlour.example - Website www.velvet-parlour.example I prefer the have the logo (without website) on the one side and the information on the other. Best regards Pieter

Target Market(s)

Art buyers / art dealers / artists / middle class / upmarket /

Industry/Entity Type

Artists

Colors

Designer to choose colors to be used in the design.

Requirements
Must have
• Must communicate credibility, trust and integrity
Nice to have
• Something classy, chique
Should not have
• Nothing to artistic or creative

```html
<!DOCTYPE html>
<html lang="en">
<head>
<meta charset="utf-8">
<title>The Velvet Parlour — Business Card</title>
<link href="https://fonts.googleapis.com/css2?family=Questrial&display=swap" rel="stylesheet">
<style>
  :root {
    --backdrop: #3a3a3a;
    --card-black: #0b0b0b;
    --card-white: #ffffff;
    --ink-dark: #1a1a1a;
    --ink-light: #f2f2f2;
    --card-shadow: rgba(0, 0, 0, 0.45);
  }
  * { margin: 0; padding: 0; box-sizing: border-box; }
  html, body {
    width: 1200px;
    height: 720px;
    overflow: hidden;
    background: var(--backdrop);
  }
  .canvas {
    position: relative;
    width: 1200px;
    height: 720px;
    display: flex;
    align-items: center;
    justify-content: center;
    gap: 60px;
    font-family: "Questrial", "Century Gothic", sans-serif;
  }
  .card {
    position: relative;
    width: 500px;
    height: 286px;
    box-shadow: 0 10px 30px var(--card-shadow);
  }
  .card--front {
    background: var(--card-black);
    color: var(--ink-light);
  }
  .brand-name {
    position: absolute;
    left: 44px;
    top: 126px;
    font-size: 24px;
    font-weight: 400;
    letter-spacing: 0.32em;
    text-transform: uppercase;
    color: var(--ink-light);
    white-space: nowrap;
  }
  .card--back {
    background: var(--card-white);
    color: var(--ink-dark);
  }
  .contact-block {
    position: absolute;
    left: 30px;
    top: 26px;
  }
  .person-name {
    font-size: 21px;
    line-height: 1.1;
  }
  .person-title {
    font-size: 13px;
    margin-top: 2px;
    margin-bottom: 10px;
  }
  .contact-line {
    font-size: 13px;
    line-height: 1.35;
  }
  .website {
    position: absolute;
    right: 30px;
    bottom: 28px;
    font-size: 15px;
  }
</style>
</head>
<body>
  <main class="canvas">
    <section class="card card--front" aria-label="Card front">
      <p class="brand-name">The Velvet Parlour</p>
    </section>

    <section class="card card--back" aria-label="Card back">
      <div class="contact-block">
        <p class="person-name">Pieter Vandomme</p>
        <p class="person-title">Founder</p>
        <p class="contact-line">Mobile: +32 (0) 486 514 362</p>
        <p class="contact-line">E-mail: pieter@velvet-parlour.example</p>
      </div>
      <p class="website">Web: www.velvet-parlour.example</p>
    </section>
  </main>
</body>
</html>
```